Brovane Grand Opening

I need a one sided flyer that advertises my grand opening for our new equipment dealership.

Grand Opening

New and Used Equipment Sales
Equipment Rentals
Residential, Commercial and Industrial Rental Equipment
Construction and Industrial Supply
Custom Metal Fabrication
Mobile Welding Service
Pickup and Delivery Service
24hr. Emergency Dedicated Service

Now Open!

4362 Marlowfield HWY
Fenmoor, SC 29000

(555) 318 - 4026

7:00am-7:00pm Monday - Friday
8:00am-3:00pm Saturday

www.brovanegear.example

```html
<!DOCTYPE html>
<html lang="en">
<head>
<meta charset="utf-8">
<title>Brovane Grand Opening</title>
<link rel="stylesheet" href="https://fonts.googleapis.com/css2?family=Archivo+Black&family=Archivo:wght@700&family=Arimo:wght@400&family=Encode+Sans+Condensed:wght@400&display=swap">
<style>
:root{
  --ink:#0b0b0b;
  --white:#ffffff;
  --maroon:#7a0f14;
  --maroon-deep:#3a0607;
  --red:#cf1f26;
  --red-dark:#8e1116;
  --brown:#5a1e10;
  --orange:#f7901e;
  --ring:#d9d4d4;
}
*{margin:0;padding:0;box-sizing:border-box}
html,body{width:954px;height:1200px;overflow:hidden;background:var(--white)}
.flyer{position:relative;width:954px;height:1200px;overflow:hidden;background:var(--white);font-family:"Arimo",Arial,sans-serif}
.hero-photo{position:absolute;left:0;top:0;width:954px;height:378px;background:linear-gradient(180deg,#eef0f1 0%,#d6d9db 40%,#6f746f 75%,#3e423d 100%)}
.services-band{position:absolute;left:0;top:393px;width:954px;height:663px;background:linear-gradient(180deg,var(--maroon) 0%,#5e0b0e 45%,var(--maroon-deep) 80%,var(--ink) 100%)}
.logo{position:absolute;left:69px;top:38px;width:312px;height:62px;background:var(--ink);border-radius:31px;display:flex;align-items:center;justify-content:center;gap:12px}
.logo-mark{width:18px;height:18px;background:var(--red)}
.logo-name{font-family:"Archivo Black",sans-serif;font-size:40px;color:var(--white);letter-spacing:1px}
.headline{position:absolute;left:410px;top:70px;width:440px;height:270px}
.photo-ring{position:absolute;border-radius:50%;border:12px solid var(--ring)}
.services{position:absolute;left:494px;top:408px;color:var(--white)}
.services-title{position:absolute;left:51px;top:6px;font-size:37px;letter-spacing:5.5px;white-space:nowrap}
.services-rule{position:absolute;left:51px;top:55px;width:255px;height:1px;background:var(--white)}
.service-list{position:absolute;left:0;top:58px;list-style:none;font-family:"Encode Sans Condensed",sans-serif;font-size:30px;line-height:33.8px;width:460px;white-space:nowrap}
.service-list li{position:relative;padding-left:30px}
.service-list li::before{content:"";position:absolute;left:2px;top:12px;width:13px;height:13px;border-radius:50%;background:var(--white)}
.hours-tab{position:absolute;left:553px;top:825px;width:268px;height:34px;background:linear-gradient(180deg,var(--red),var(--red-dark));border-radius:16px;color:var(--white);font-size:28px;text-align:center;line-height:34px}
.hours-tab::after{content:"";position:absolute;left:120px;top:33px;border-left:14px solid transparent;border-right:14px solid transparent;border-top:14px solid var(--red-dark)}
.hours-row{position:absolute;height:35px;background:var(--white);border-radius:18px;display:flex;align-items:center}
.hours-day{height:100%;background:var(--orange);border-radius:18px;color:var(--white);font-size:25px;display:flex;align-items:center;justify-content:center}
.hours-time{font-size:25px;color:var(--ink);padding-left:18px}
.enquiry{position:absolute;left:242px;top:1009px;width:471px;height:27px;background:var(--red);border-radius:14px;color:var(--white);font-size:24px;letter-spacing:14px;text-align:center;line-height:27px;padding-left:14px}
.contact{position:absolute;font-family:"Archivo",sans-serif;font-weight:700;color:var(--ink);white-space:nowrap}
.contact-plain{position:absolute;color:var(--ink);font-size:21px;white-space:nowrap}
.icon{position:absolute}
.social-dot{position:absolute;left:535px;top:1107px;width:20px;height:20px;border-radius:50%;background:var(--ink)}
</style>
</head>
<body>
<div class="flyer">
  <div class="hero-photo" role="img" aria-label="Equipment yard with machinery, power pole and trees under an overcast sky"></div>
  <div class="services-band"></div>

  <div class="logo"><span class="logo-mark"></span><span class="logo-name">Brovane</span></div>

  <svg class="headline" viewBox="0 0 440 270" aria-label="Grand Opening Now">
    <defs>
      <linearGradient id="headFill" x1="0" y1="0" x2="0" y2="1">
        <stop offset="0" stop-color="#e0303a"/><stop offset="1" stop-color="#9a1218"/>
      </linearGradient>
    </defs>
    <g transform="rotate(-4 220 135)" font-family="Archivo Black, sans-serif" fill="url(#headFill)" stroke="#5a1e10" stroke-width="7" paint-order="stroke" text-anchor="middle">
      <text x="225" y="95" font-size="84">GRAND</text>
      <text x="220" y="170" font-size="84">OPENING</text>
      <text x="235" y="250" font-size="100" stroke="#ffffff" stroke-width="5" fill="#d4222a">NOW</text>
    </g>
  </svg>

  <div class="photo-ring" style="left:23px;top:161px;width:246px;height:246px;background:linear-gradient(160deg,#8fb0d6,#7aa25a 40%,#c42a22 70%,#5a5a5a)" role="img" aria-label="Red farm implement and generator on a grassy lot"></div>
  <div class="photo-ring" style="left:-16px;top:442px;width:262px;height:262px;background:linear-gradient(160deg,#c9d8e8,#93a0a8 35%,#d9391f 65%,#6a6a66)" role="img" aria-label="Orange compact tractor parked on gravel"></div>
  <div class="photo-ring" style="left:200px;top:307px;width:254px;height:254px;background:linear-gradient(160deg,#7a7a74,#c98a2a 40%,#b8761f 65%,#2e2e2e)" role="img" aria-label="Trailer-mounted portable generator"></div>
  <div class="photo-ring" style="left:196px;top:580px;width:262px;height:262px;background:linear-gradient(160deg,#8fb4e0,#7a9a6a 30%,#e8b22a 60%,#8a8a84)" role="img" aria-label="Yellow skid steer loader on a gravel lot"></div>

  <div class="services">
    <div class="services-title">Our Services</div>
    <div class="services-rule"></div>
    <ul class="service-list">
      <li>New and Used Equipment Sales</li>
      <li>Equipment Rentals</li>
      <li>Residential, Commercial and<br>&nbsp;Industrial Rental Equipment</li>
      <li>Construction and Industrial<br>Supply</li>
      <li>Custom Metal Fabrication</li>
      <li>Mobile Welding Service</li>
      <li>Pickup and Delivery Service</li>
      <li>24hr. Emergency Dedicated Service</li>
    </ul>
  </div>

  <div class="hours-tab">Open Hours</div>
  <div class="hours-row" style="left:486px;top:886px;width:412px"><span class="hours-day" style="width:175px">MON - FRI</span><span class="hours-time">7:00am - 7:00pm</span></div>
  <div class="hours-row" style="left:480px;top:938px;width:418px"><span class="hours-day" style="width:175px">SATURDAY</span><span class="hours-time">8:00am - 3:00pm</span></div>

  <div class="enquiry">ENQUIRY</div>

  <svg class="icon" style="left:230px;top:1063px" width="28" height="28" viewBox="0 0 28 28"><circle cx="14" cy="14" r="14" fill="#0b0b0b"/><path d="M14 6a5.5 5.5 0 0 0-5.5 5.5c0 4 5.5 10 5.5 10s5.5-6 5.5-10A5.5 5.5 0 0 0 14 6z" fill="#fff"/><circle cx="14" cy="11.5" r="2.2" fill="#0b0b0b"/></svg>
  <div class="contact" style="left:278px;top:1059px;font-size:19px">FENMOOR, SC</div>
  <div class="contact" style="left:271px;top:1083px;font-size:19px;line-height:24px">4362 Marlowfield HWY<br>Fenmoor, SC 29000</div>

  <svg class="icon" style="left:532px;top:1061px" width="27" height="27" viewBox="0 0 28 28"><circle cx="14" cy="14" r="14" fill="#0b0b0b"/><path d="M10 7l3 4-2 2c1 2 3 4 5 5l2-2 4 3-2 3c-6 0-13-7-13-13z" fill="#fff"/></svg>
  <div class="contact-plain" style="left:566px;top:1060px">(555) 318 - 4026</div>

  <span class="social-dot"></span>
  <div class="contact-plain" style="left:566px;top:1105px">brovanegear</div>

  <svg class="icon" style="left:338px;top:1143px" width="27" height="27" viewBox="0 0 28 28"><circle cx="14" cy="14" r="14" fill="#0b0b0b"/><g fill="none" stroke="#fff" stroke-width="1.6"><circle cx="14" cy="14" r="8"/><ellipse cx="14" cy="14" rx="3.5" ry="8"/><path d="M6 14h16M8 10h12M8 18h12"/></g></svg>
  <div class="contact-plain" style="left:374px;top:1143px;font-size:23px">www.brovanegear.example</div>
</div>
</body>
</html>
```